Plakat-Design für Zimmerei
Zielgruppe
Wir sind eine Zimmerei traditionell geprägte Zimmerei, die ihr Hauptaugenmerk auf Qualität und Zuverlässigkeit legt. Zur Zeit umfasst die Zimmerei Holger Brandt neben dem Inhaber zwei weitere Zimmerergesellen, einen Auszubildenden und einen Praktikanten.
Unsere Zielgruppe sind alle Personen- und Unternehmensgruppen in der nahen Umgebung, welche Zimmererarbeiten in Anspruch nehmen wollen.
Aufgabenstellung
Unsere Plakatwerbung soll vor allem Einfach und Übersichtlich gehalten werden.
Folgende Infos sollen dargestellt werden:
Zimmerei Holger Brandt
Aus dem Banner soll erstellt werden:
Baugerüstplanen: 200 cm x 205 cm
Bauzaunbanner: 340 cm x 173 cm
Schilder: 70 cm x 100 cm

```html
<!DOCTYPE html>
<html lang="de">
<head>
<meta charset="utf-8">
<title>Zimmerei Holger Brandt – Plakat</title>
<link rel="stylesheet" href="https://fonts.googleapis.com/css2?family=Arvo:wght@700&family=Roboto+Slab:wght@300;700&family=Mulish:ital,wght@1,400&display=swap">
<style>
  :root {
    --wood-dark: #3e362e;
    --wood-mid: #5f554a;
    --wood-light: #7a6e60;
    --panel: #625a50;
    --white: #ffffff;
    --gold: #e3b022;
    --roof-light: #d9b57d;
    --roof-mid: #b88452;
    --roof-dark: #7a5433;
  }
  html, body { margin: 0; padding: 0; overflow: hidden; background: var(--wood-dark); }
  .poster {
    position: relative;
    width: 849px;
    height: 1200px;
    overflow: hidden;
    background: var(--panel);
  }
  .wood-backdrop {
    position: absolute; inset: 0;
    background:
      linear-gradient(180deg, rgba(0,0,0,0.18) 0%, rgba(0,0,0,0) 40%),
      repeating-linear-gradient(180deg, var(--wood-mid) 0 64px, var(--wood-dark) 64px 66px),
      var(--wood-mid);
  }
  .tools-photo {
    position: absolute; left: 0; top: 0; width: 849px; height: 290px;
    background: linear-gradient(180deg, rgba(40,34,28,0.55), rgba(40,34,28,0));
  }
  .info-panel {
    position: absolute; left: 0; top: 525px; width: 849px; height: 586px;
    background: var(--panel);
  }
  .brand-mark {
    position: absolute; left: 349px; top: 253px; width: 188px; height: 188px;
    display: flex; align-items: center; justify-content: center; gap: 8px;
  }
  .brand-mark__dot {
    width: 18px; height: 18px; border-radius: 50%; background: var(--white);
  }
  .brand-mark__name {
    font-family: "Arvo", "Roboto Slab", serif; font-weight: 700;
    color: var(--white); font-size: 22px; line-height: 1.1; text-align: center;
  }
  .headline {
    position: absolute; left: 0; width: 849px; top: 466px; margin: 0;
    text-align: center; padding-left: 40px; box-sizing: border-box;
    font-family: "Arvo", "Roboto Slab", serif; font-weight: 700;
    font-size: 46px; color: var(--white); letter-spacing: 0.5px;
  }
  .contact {
    position: absolute; left: 0; width: 410px; text-align: center;
    color: var(--white);
    font-family: "Roboto Slab", serif; font-weight: 300;
  }
  .tagline {
    top: 582px; font-family: "Mulish", sans-serif; font-style: italic;
    color: var(--gold); font-size: 23px; line-height: 33px; margin: 0;
  }
  .contact p { margin: 0; font-size: 24px; line-height: 33px; }
  .owner { top: 722px; }
  .address { top: 822px; }
  .phones { top: 923px; }
  .email { top: 1024px; }
  .website {
    position: absolute; left: 0; width: 410px; top: 1150px; text-align: center;
    font-family: "Roboto Slab", serif; font-weight: 700; font-size: 21px;
    color: var(--white); letter-spacing: 0.3px;
  }
  .project-photo { position: absolute; left: 397px; width: 422px; }
  .project-photo--dome {
    top: 553px; height: 316px;
    background: radial-gradient(circle at 42% 22%, var(--roof-light) 0%, var(--roof-mid) 70%, var(--roof-dark) 100%);
  }
  .project-photo--rafters {
    top: 890px; height: 310px;
    background: linear-gradient(160deg, var(--roof-dark) 0%, var(--roof-mid) 55%, var(--roof-light) 100%);
  }
</style>
</head>
<body>
<div class="poster">
  <div class="wood-backdrop" role="img" aria-label="Holzbretter-Hintergrund in dunklem Braun"></div>
  <div class="tools-photo" role="img" aria-label="Foto von alten Werkzeugen auf Holzbrettern: Rohrzange, Hammer, Zange, Schraubendreher, Fäustel"></div>
  <div class="info-panel"></div>

  <div class="brand-mark">
    <span class="brand-mark__dot"></span>
    <span class="brand-mark__name">Zimmerei<br>Brandt</span>
  </div>

  <h1 class="headline">Zimmerei Holger Brandt</h1>

  <p class="contact tagline">Ihr traditioneller<br>Meisterbetrieb<br>seit 1975!</p>

  <div class="contact owner"><p>Inh. Holger Brandt</p><p>Zimmerermeister</p></div>
  <div class="contact address"><p>Eichenhainweg 12</p><p>56410 Talbach</p></div>
  <div class="contact phones"><p>Telefon: 0264 / 58213</p><p>Handy: 01739054426</p></div>
  <div class="contact email"><p>info@zimmerei-brandt.de</p></div>

  <div class="website">www.zimmerei-brandt.de</div>

  <div class="project-photo project-photo--dome" role="img" aria-label="Foto einer achteckigen Holzdecke mit sternförmig zulaufenden Sparren"></div>
  <div class="project-photo project-photo--rafters" role="img" aria-label="Foto eines offenen Dachstuhls mit Sparren und Lattung von innen"></div>
</div>
</body>
</html>
```